Corvanta512 Business Card Redesign

I want to create a design for brand new business cards, I need something exceptional for clear plastic business card design. Please do not submit without it being on a clear design. Photos of the various logo versions attached.

```html
<!DOCTYPE html>
<html lang="en">
<head>
<meta charset="UTF-8">
<title>Corvanta512 Clear Business Cards</title>
<link href="https://fonts.googleapis.com/css2?family=EB+Garamond:wght@400;500;600&display=swap" rel="stylesheet">
<style>
  :root {
    --bg: #1d1e22;
    --frost: rgba(255, 255, 255, 0.86);
    --clear-rim: rgba(255, 255, 255, 0.22);
    --clear-edge: rgba(255, 255, 255, 0.55);
    --navy: rgba(42, 64, 104, 0.92);
    --navy-tint: rgba(35, 58, 96, 0.78);
    --navy-light: rgba(120, 145, 190, 0.55);
    --gold: #c9a551;
    --ink: #1c1c1c;
    --muted: #555555;
  }
  * { margin: 0; padding: 0; box-sizing: border-box; }
  html, body { width: 1200px; height: 900px; overflow: hidden; }
  body {
    background: var(--bg);
    font-family: "EB Garamond", Georgia, serif;
    position: relative;
  }

  /* clear plastic card shell: transparent rim, frosted print area */
  .card {
    position: absolute;
    top: 296px;
    width: 540px;
    height: 308px;
    border-radius: 18px;
    overflow: hidden;
    border: 10px solid var(--clear-rim);
    background-clip: padding-box;
    box-shadow:
      0 0 0 1px var(--clear-edge),
      inset 0 0 0 1px rgba(255, 255, 255, 0.35),
      0 18px 40px rgba(0, 0, 0, 0.45);
  }
  .card::after {
    content: "";
    position: absolute;
    inset: 0;
    background: linear-gradient(125deg, rgba(255,255,255,0.28) 0%, rgba(255,255,255,0) 38%, rgba(255,255,255,0) 70%, rgba(255,255,255,0.12) 100%);
    pointer-events: none;
  }
  .card--front { left: 40px; background-color: var(--frost); }
  .card--back { left: 620px; background-color: var(--navy-tint); }

  /* front */
  .front__content {
    position: absolute;
    left: 0; right: 0; top: 24px;
    text-align: center;
    color: var(--ink);
  }
  .brand-mark {
    display: inline-flex;
    align-items: center;
    gap: 10px;
  }
  .brand-mark__dot {
    width: 16px; height: 16px; border-radius: 50%;
    background: var(--gold);
  }
  .brand-mark__name {
    color: var(--gold);
    font-weight: 600;
    letter-spacing: 2px;
    text-transform: uppercase;
  }
  .front .brand-mark__name { font-size: 30px; }
  .person__name {
    margin-top: 6px;
    font-size: 30px;
    letter-spacing: 1px;
    text-transform: uppercase;
    font-weight: 500;
    line-height: 1.15;
  }
  .person__role {
    font-size: 13px;
    letter-spacing: 5px;
    color: var(--muted);
    text-transform: uppercase;
  }
  .contact-row {
    display: flex;
    justify-content: center;
    gap: 26px;
    margin-top: 10px;
    font-size: 17px;
  }
  .contact-item { display: inline-flex; align-items: center; gap: 7px; }
  .contact-item svg { width: 15px; height: 15px; }
  .front__band {
    position: absolute;
    left: 0; right: 0; bottom: 0;
    height: 58px;
  }
  .front__band svg { position: absolute; inset: 0; width: 100%; height: 100%; }
  .front__address {
    position: absolute;
    left: 0; right: 0; bottom: 12px;
    display: flex; justify-content: center; align-items: center; gap: 8px;
    color: #ffffff;
    font-size: 17px;
  }
  .front__address svg { width: 14px; height: 16px; }

  /* back */
  .back__sheen {
    position: absolute; inset: 0; width: 100%; height: 100%;
  }
  .back__brand {
    position: absolute;
    inset: 0;
    display: flex; align-items: center; justify-content: center;
  }
  .back__brand .brand-mark { gap: 16px; }
  .back__brand .brand-mark__dot { width: 26px; height: 26px; }
  .back__brand .brand-mark__name { font-size: 50px; letter-spacing: 3px; }
</style>
</head>
<body>

<section class="card card--front front">
  <div class="front__content">
    <div class="brand-mark">
      <span class="brand-mark__dot"></span>
      <span class="brand-mark__name">Corvanta512</span>
    </div>
    <h1 class="person__name">Marisa Colwell</h1>
    <p class="person__role">Founder</p>
    <div class="contact-row">
      <span class="contact-item">
        <svg viewBox="0 0 16 16"><path fill="#c9a551" d="M3 1l3 3-1.5 2a9 9 0 0 0 5.5 5.5L12 10l3 3-2 2C7 15 1 9 1 3z"/></svg>
        +11 44-56-7890
      </span>
      <span class="contact-item">
        <svg viewBox="0 0 16 16"><circle cx="8" cy="8" r="7" fill="none" stroke="#c9a551" stroke-width="1.6"/><ellipse cx="8" cy="8" rx="3" ry="7" fill="none" stroke="#c9a551" stroke-width="1.4"/><line x1="1" y1="8" x2="15" y2="8" stroke="#c9a551" stroke-width="1.4"/></svg>
        www.corvanta512.com
      </span>
    </div>
    <div class="contact-row">
      <span class="contact-item">
        <svg viewBox="0 0 16 16"><rect x="1" y="3" width="14" height="10" fill="#c9a551"/><path d="M1 3l7 6 7-6" fill="none" stroke="#ffffff" stroke-width="1.2"/></svg>
        info@corvanta512.com
      </span>
    </div>
  </div>
  <div class="front__band">
    <svg viewBox="0 0 520 58" preserveAspectRatio="none">
      <polygon points="0,58 0,44 66,44 76,0 444,0 454,12 520,12 520,58" fill="rgba(42,64,104,0.92)"/>
    </svg>
  </div>
  <p class="front__address">
    <svg viewBox="0 0 14 16"><path fill="#ffffff" d="M7 0a5.5 5.5 0 0 0-5.5 5.5C1.5 10 7 16 7 16s5.5-6 5.5-10.5A5.5 5.5 0 0 0 7 0zm0 7.6a2 2 0 1 1 0-4 2 2 0 0 1 0 4z"/></svg>
    18 Harbor Lane, Easton, NY 10020, USA
  </p>
</section>

<section class="card card--back">
  <svg class="back__sheen" viewBox="0 0 520 288" preserveAspectRatio="none">
    <path d="M0,0 H520 V64 Q290,74 0,140 Z" fill="rgba(120,145,190,0.55)"/>
  </svg>
  <div class="back__brand">
    <div class="brand-mark">
      <span class="brand-mark__dot"></span>
      <span class="brand-mark__name">Corvanta512</span>
    </div>
  </div>
</section>

</body>
</html>
```